Ferrant Valley Zoning Council Business Cards

We're looking for a business card design, simple as that. We're a local government agency that mainly performs building code enforcement, transportation planning, floodplain management, and GIS for Tobelle Parish in Louisiana, and other surround parishes. So you're not having to Google anything, GIS is, at it's core, mapping. Building Code Enforcement is just that, nothing more. Floodplain Management is to make sure the public is within what the government

Contact Information for Business Card

Our Address is

517 Marwick Street
Alexandria, LA 71489

Our phone is 3185529137
Our fax is 3185529142
Our website is www.fvzc.info
My email is dana@fvzc.info

Font styles to use
Serif
Sans Serif

Colors

Designer to choose colors to be used in the design.

Requirements
Must have
• I'm attaching our logo(several versions) that must be incorporated. The design should fit well with our existing logo. I can send photoshop files for our logo if needed. If possible, I'd like to be able to add names/info to each card for all of our employees once this is done.
Nice to have
• The Louisiana state seal is a bonus, and isn't specifically required.

```html
<!DOCTYPE html>
<html lang="en">
<head>
<meta charset="utf-8">
<title>Ferrant Valley Zoning Council – Business Cards</title>
<link rel="stylesheet" href="https://fonts.googleapis.com/css2?family=Open+Sans:wght@400;700&display=swap">
<style>
  :root {
    --backdrop: #1c1c1c;
    --card-dark: #0d0d0d;
    --card-light: #ffffff;
    --ink: #111111;
    --ink-soft: #3a3a3a;
    --white: #ffffff;
    --accent-green: #5fb82e;
    --seal-navy: #1d3f7a;
    --divider: #d9d9d9;
  }
  * { margin: 0; padding: 0; box-sizing: border-box; }
  html, body {
    width: 1200px; height: 900px; overflow: hidden;
    background: var(--backdrop);
    font-family: "Open Sans", Arial, sans-serif;
  }
  .canvas {
    position: relative; width: 1200px; height: 900px;
  }
  .card {
    position: absolute; left: 320px; width: 560px; height: 320px;
    box-shadow: 0 10px 30px rgba(0,0,0,.55);
  }
  .card--front { top: 90px; background: var(--card-dark); }
  .card--back { top: 490px; background: var(--card-light); }

  .wordmark {
    position: absolute; display: flex; align-items: center; gap: 12px;
    font-weight: 700; letter-spacing: 1px;
  }
  .wordmark__square { width: 34px; height: 34px; background: var(--accent-green); }
  .card--front .wordmark { left: 150px; top: 128px; color: var(--white); font-size: 52px; line-height: 1; }
  .card--back .wordmark { left: 44px; top: 128px; color: var(--ink); font-size: 54px; line-height: 1; }

  .seal {
    position: absolute; left: 430px; top: 116px; width: 76px; height: 76px;
    border-radius: 50%; background: var(--seal-navy); border: 4px solid var(--white);
  }

  .card__divider {
    position: absolute; left: 282px; top: 0; width: 1px; height: 320px;
    background: var(--divider);
    box-shadow: 4px 0 10px rgba(0,0,0,.06);
  }
  .contact {
    position: absolute; left: 312px; top: 54px; color: var(--ink-soft);
    font-size: 15px; line-height: 20px;
  }
  .contact__name { color: var(--ink); font-weight: 700; font-size: 17px; letter-spacing: .3px; }
  .contact__title { margin-bottom: 6px; }
  .contact__row { display: flex; align-items: center; gap: 8px; }
  .contact__row svg { width: 14px; height: 14px; fill: var(--ink); flex: none; }
  .contact__address { margin-top: 4px; padding-left: 22px; }
</style>
</head>
<body>
<main class="canvas">
  <section class="card card--front" aria-label="Card front">
    <div class="wordmark"><span class="wordmark__square"></span>FVZC</div>
    <div class="seal" role="img" aria-label="State seal badge"></div>
  </section>

  <section class="card card--back" aria-label="Card back">
    <div class="wordmark"><span class="wordmark__square"></span>FVZC</div>
    <div class="card__divider"></div>
    <div class="contact">
      <div class="contact__name">CARTER HOLLIS</div>
      <div class="contact__title">Managing Director</div>
      <div class="contact__row">
        <svg viewBox="0 0 16 16" aria-hidden="true"><path d="M3 2h3l1.5 3.5-2 1.2a8 8 0 0 0 3.8 3.8l1.2-2L14 10v3a1 1 0 0 1-1 1A11 11 0 0 1 2 3a1 1 0 0 1 1-1z"/></svg>
        <span>3185529137</span>
      </div>
      <div class="contact__row">
        <svg viewBox="0 0 16 16" aria-hidden="true"><path d="M4 1h8v4H4zM2 6h12a1 1 0 0 1 1 1v5h-3v3H4v-3H1V7a1 1 0 0 1 1-1zm3 5v3h6v-3z"/></svg>
        <span>3185529142</span>
      </div>
      <div class="contact__row">
        <svg viewBox="0 0 16 16" aria-hidden="true"><path d="M1 3h14v10H1zm1.5 1.5L8 9l5.5-4.5z"/></svg>
        <span>dana@fvzc.info</span>
      </div>
      <div class="contact__row">
        <svg viewBox="0 0 16 16" aria-hidden="true"><circle cx="8" cy="8" r="7"/></svg>
        <span>www.fvzc.info</span>
      </div>
      <div class="contact__address">517 Marwick Street<br>Alexandria, LA 71489</div>
    </div>
  </section>
</main>
</body>
</html>
```